BrickaFun Business Card

We need a business card design for our company. We sell construction-themed amusement rides for kids.

Contact Information for Business Card

Contact info on business card should include:
Dale Hurst
Co-Founder & COO
(833) 517-BRICKAF
Dale@brickafun.com
www.brickafun.com

```html
<!DOCTYPE html>
<html lang="en">
<head>
<meta charset="utf-8">
<title>BrickaFun Business Card</title>
<link rel="stylesheet" href="https://fonts.googleapis.com/css2?family=Roboto:wght@400;700&display=swap">
<style>
  :root {
    --backdrop: #e4e4e6;
    --card: #f7f7f8;
    --brand-orange: #e2511c;
    --accent-purple: #8a1e96;
    --text-grey: #555559;
    --rule: #cfcfd3;
  }
  * { margin: 0; padding: 0; box-sizing: border-box; }
  html, body { width: 1200px; height: 800px; overflow: hidden; }
  body {
    background: var(--backdrop);
    font-family: "Roboto", Arial, sans-serif;
    display: flex;
    flex-direction: column;
    align-items: center;
    justify-content: center;
    gap: 60px;
  }
  .card {
    width: 560px;
    height: 320px;
    background: var(--card);
    border-radius: 22px;
    box-shadow: 0 10px 28px rgba(0,0,0,0.16);
    position: relative;
    display: flex;
    align-items: center;
  }
  .brand-name {
    color: var(--brand-orange);
    font-weight: 700;
    letter-spacing: 0.5px;
    white-space: nowrap;
  }
  .card--front .brand-block {
    width: 290px;
    display: flex;
    justify-content: center;
  }
  .card--front .brand-name { font-size: 40px; }
  .divider {
    width: 1px;
    height: 90px;
    background: var(--rule);
  }
  .contact {
    padding-left: 26px;
    color: var(--text-grey);
  }
  .contact-name {
    color: var(--accent-purple);
    font-weight: 700;
    font-size: 20px;
  }
  .contact-title {
    font-size: 14px;
    margin-top: 2px;
    margin-bottom: 12px;
  }
  .contact-list { list-style: none; }
  .contact-list li {
    display: flex;
    align-items: center;
    gap: 8px;
    font-size: 13px;
    line-height: 22px;
  }
  .contact-list svg { width: 13px; height: 13px; flex: none; }
  .card--back { justify-content: center; }
  .card--back .brand-name { font-size: 64px; }
</style>
</head>
<body>
  <section class="card card--front" aria-label="Business card front">
    <div class="brand-block"><span class="brand-name">BrickaFun</span></div>
    <div class="divider"></div>
    <div class="contact">
      <p class="contact-name">Dale Hurst</p>
      <p class="contact-title">Co-Founder &amp; COO</p>
      <ul class="contact-list">
        <li>
          <svg viewBox="0 0 16 16" aria-hidden="true"><path fill="#8a1e96" d="M3.6 1.2l2.3 2.6-1.2 1.8c.9 2 2.6 3.8 4.7 4.8l1.8-1.2 2.6 2.3-1.3 2.5C7.4 13.7 2.3 8.6 1.2 2.5z"/></svg>
          (833) 517-BRICKAF
        </li>
        <li>
          <svg viewBox="0 0 16 16" aria-hidden="true"><rect x="1" y="3" width="14" height="10" rx="1.5" fill="#8a1e96"/><path d="M2 4.5l6 4.5 6-4.5" stroke="#fff" stroke-width="1.4" fill="none"/></svg>
          Dale@brickafun.com
        </li>
        <li>
          <svg viewBox="0 0 16 16" aria-hidden="true"><circle cx="8" cy="8" r="7" fill="#8a1e96"/><path d="M1 8h14M8 1c-3 3.5-3 10.5 0 14M8 1c3 3.5 3 10.5 0 14" stroke="#fff" stroke-width="1" fill="none"/></svg>
          www.brickafun.com
        </li>
      </ul>
    </div>
  </section>

  <section class="card card--back" aria-label="Business card back">
    <span class="brand-name">BrickaFun</span>
  </section>
</body>
</html>
```